New Advertising Company Business Card

A two sided business card. One side with logo only and the other side with my information and maybe my logo again. Looking for something unique and creative, but not too busy. Info would include my name(Marcus Feldon), President, phone number, address, email address, and website. LOGO IS THE BLUE AND WHITE ONE.

Target Market(s)

CEO/VP Level Audience

Industry/Entity Type

Business

Contact Information for Business Card

In Description.

```html
<!DOCTYPE html>
<html lang="en">
<head>
<meta charset="UTF-8">
<title>Lumen Advertising – Business Card</title>
<link href="https://fonts.googleapis.com/css2?family=Montserrat:wght@500;600;700&family=Open+Sans:wght@400&display=swap" rel="stylesheet">
<style>
  :root {
    --page-bg: #f3f3f3;
    --card-white: #ffffff;
    --card-dark: #222222;
    --brand-blue: #1175c2;
    --ink: #222222;
    --muted: #555555;
    --light: #ffffff;
  }
  * { margin: 0; padding: 0; box-sizing: border-box; }
  html, body {
    width: 1200px; height: 1200px; overflow: hidden;
    background: var(--page-bg);
  }
  .canvas { position: relative; width: 1200px; height: 1200px; }
  .card {
    position: absolute; left: 171px; width: 869px; height: 485px;
    border-radius: 32px; overflow: hidden;
  }
  .card--front { top: 85px; background: var(--card-white); }
  .card--back  { top: 634px; background: var(--card-dark); }

  .card__shape { position: absolute; inset: 0; }

  .person { position: absolute; left: 57px; top: 50px; }
  .person__name {
    font-family: "Montserrat", sans-serif; font-weight: 700;
    font-size: 35px; color: var(--brand-blue); line-height: 1;
  }
  .person__role {
    font-family: "Open Sans", sans-serif; font-size: 21px;
    color: var(--muted); margin-top: 8px;
  }

  .contact-list {
    position: absolute; left: 55px; top: 318px; list-style: none;
    font-family: "Open Sans", sans-serif; font-size: 21px; color: var(--light);
  }
  .contact-list li { display: flex; align-items: center; height: 30.5px; }
  .contact-list svg { width: 18px; height: 18px; margin-right: 10px; flex: none; }

  .brand {
    position: absolute; font-family: "Montserrat", sans-serif;
    font-weight: 600; text-transform: uppercase; line-height: 1;
  }
  .brand__main { display: block; font-size: 62px; letter-spacing: 6px; }
  .brand__sub  { display: block; font-size: 26px; letter-spacing: 11px; margin-top: 12px; }
  .brand--front { right: 55px; top: 158px; text-align: right; color: var(--ink); }
  .brand--back  { left: 0; right: 0; top: 250px; text-align: center; color: var(--light); }

  .address {
    position: absolute; right: 55px; top: 375px; text-align: right;
    font-family: "Open Sans", sans-serif; font-size: 21px;
    color: var(--muted); line-height: 30px;
  }

  .web {
    position: absolute; left: 0; right: 0; top: 424px; text-align: center;
    font-family: "Montserrat", sans-serif; font-weight: 500;
    font-size: 19px; letter-spacing: 2px; color: var(--light);
  }
  .web__accent { color: var(--brand-blue); }
</style>
</head>
<body>
<main class="canvas">

  <section class="card card--front" aria-label="Card front">
    <svg class="card__shape" viewBox="0 0 869 485" preserveAspectRatio="none" aria-hidden="true">
      <path d="M0,320 C60,190 120,136 176,136 C280,136 400,300 432,485 L0,485 Z" fill="var(--brand-blue)"/>
      <path d="M0,348 C50,230 100,170 160,170 C260,170 370,320 408,485 L0,485 Z" fill="var(--card-dark)"/>
    </svg>

    <div class="person">
      <h1 class="person__name">Marcus Feldon</h1>
      <p class="person__role">President</p>
    </div>

    <ul class="contact-list">
      <li>
        <svg viewBox="0 0 24 24" aria-hidden="true"><path fill="var(--brand-blue)" d="M6.6 10.8a15 15 0 0 0 6.6 6.6l2.2-2.2c.3-.3.7-.4 1-.2 1.1.4 2.3.6 3.6.6.6 0 1 .4 1 1V20c0 .6-.4 1-1 1A17 17 0 0 1 3 4c0-.6.4-1 1-1h3.5c.6 0 1 .4 1 1 0 1.3.2 2.5.6 3.6.1.3 0 .7-.2 1z"/></svg>
        <span>+000.000.00 00</span>
      </li>
      <li>
        <svg viewBox="0 0 24 24" aria-hidden="true"><rect x="6" y="2" width="12" height="20" rx="2" fill="none" stroke="var(--brand-blue)" stroke-width="2.5"/><circle cx="12" cy="18" r="1.2" fill="var(--brand-blue)"/></svg>
        <span>+000.000.00 00</span>
      </li>
      <li>
        <svg viewBox="0 0 24 24" aria-hidden="true"><rect x="2" y="5" width="20" height="14" fill="var(--brand-blue)"/><path d="M2 5l10 8 10-8M2 19l7-6M22 19l-7-6" fill="none" stroke="var(--card-dark)" stroke-width="1.5"/></svg>
        <span>info@yourmailaddress.com</span>
      </li>
      <li>
        <svg viewBox="0 0 24 24" aria-hidden="true"><g fill="none" stroke="var(--brand-blue)" stroke-width="2"><circle cx="12" cy="12" r="10"/><ellipse cx="12" cy="12" rx="4.5" ry="10"/><path d="M2 12h20M4 7h16M4 17h16"/></g></svg>
        <span>www.yourmailaddress.com</span>
      </li>
    </ul>

    <div class="brand brand--front">
      <span class="brand__main">Lumen</span>
      <span class="brand__sub">Advertising</span>
    </div>

    <address class="address" style="font-style: normal;">
      Street Name Avenue, Suite<br>
      100 State, Zip Code,Country
    </address>
  </section>

  <section class="card card--back" aria-label="Card back">
    <div class="brand brand--back">
      <span class="brand__main">Lumen</span>
      <span class="brand__sub">Advertising</span>
    </div>
    <p class="web"><span class="web__accent">www.</span>yourwebaddress<span class="web__accent">.com</span></p>
  </section>

</main>
</body>
</html>
```